Magazine advertisement for wedding proposal

SPECS
Page size: 221,0-290,0
File format:Certified PDF PrintSpec_7Q2 (CMYK).
supply with crop marks on sheet mirror format
boundlessly knitted

CONTENT
I am going to ask my wife to marry me (again). I have bought a 1/1 page in her favourite Glossy. I would like the advertisement to present a letter from a type machine covered with some polaroid pictures of her. Idea is to mimic a guy in love writing a letter and dreaming away at her pictures. I would like the whole look and feel to be professional and in style. As such colours etc. may be changed and altered to make it a great integrated piece. I have added multiple pohoto's. Not all have to be used. You can choose which and how much you find most appealing. I At least want Photo Mara 1 to be used and one of the pictures with us together in white (couple).

The letter should read the following text:

Once in your lifetime you meet someone who changes everything.
She is going to do her thing with or without you. That's why she is a queen.

But we are just better together, babe...☺
That's why I want you to love me, stay with me and marry me. Would you?

Marieke,

Wil je met me trouwen?

-xxx-

Dorian

Requirements
Must have
• Be creative! This is just my first thought, but if you have an idea which you think is better, please let me know.
• - light & warm colours which all have the same look and feel (I do not like too much accent and opposite colours)
• - text as a love letter or poem
• - usage of Photo Mara 1
• - usage of couple photo
• - usage of both photo's with kids
Should not have
• - too cliché props - one or two things like hearts and flowers is ok, but dont overdo it

```html
<!DOCTYPE html>
<html lang="en">
<head>
<meta charset="utf-8">
<title>Wil je met me trouwen?</title>
<link rel="stylesheet" href="https://fonts.googleapis.com/css2?family=Special+Elite&display=swap">
<style>
  :root {
    --paper: #f1ece1;
    --paper-edge: #ddd3bf;
    --ink: #1d1b19;
    --frame: #fbfbf9;
    --shadow: rgba(60, 45, 25, 0.28);
    --night-blue: #0d2a55;
    --night-deep: #0a2144;
    --sunny-cream: #d9c8b0;
    --sunny-blue: #9fb7d6;
    --warm-red: #b5483a;
    --warm-skin: #d9a98a;
  }
  * { margin: 0; padding: 0; box-sizing: border-box; }
  html, body { width: 915px; height: 1200px; overflow: hidden; }
  body { background: var(--paper); }
  .page {
    position: relative;
    width: 915px;
    height: 1200px;
    overflow: hidden;
    background:
      radial-gradient(ellipse at 50% 45%, #f7f3ea 0%, var(--paper) 55%, var(--paper-edge) 100%);
  }
  .polaroid {
    position: absolute;
    background: var(--frame);
    box-shadow: 0 6px 14px var(--shadow), 0 1px 3px rgba(0,0,0,0.15);
  }
  .polaroid .photo {
    position: absolute;
    left: 5.5%;
    top: 5.5%;
    width: 89%;
    height: 76%;
  }
  .polaroid--couple {
    left: 301px; top: 78px; width: 358px; height: 338px;
    transform: rotate(-6deg);
  }
  .polaroid--couple .photo {
    background: radial-gradient(ellipse at 50% 60%, var(--night-blue) 0%, var(--night-deep) 100%);
  }
  .polaroid--portrait {
    left: 133px; top: 268px; width: 348px; height: 356px;
    transform: rotate(-5deg);
  }
  .polaroid--portrait .photo {
    background: linear-gradient(160deg, #7a6a5a 0%, var(--sunny-cream) 45%, var(--sunny-blue) 100%);
  }
  .polaroid--together {
    left: 466px; top: 334px; width: 330px; height: 320px;
    transform: rotate(5deg);
  }
  .polaroid--together .photo {
    background: linear-gradient(110deg, var(--warm-red) 0%, var(--warm-skin) 45%, #6b4a35 75%, #2a2a33 100%);
  }
  .letter {
    position: absolute;
    left: 88px;
    top: 735px;
    width: 740px;
    font-family: "Special Elite", "Courier New", monospace;
    font-size: 23px;
    line-height: 33px;
    color: var(--ink);
    text-align: center;
  }
  .letter p { margin-bottom: 33px; }
  .letter p:last-child { margin-bottom: 0; }
</style>
</head>
<body>
  <main class="page">
    <figure class="polaroid polaroid--couple">
      <div class="photo" role="img" aria-label="Photo of the couple dressed in white embracing against a deep blue sky"></div>
    </figure>
    <figure class="polaroid polaroid--portrait">
      <div class="photo" role="img" aria-label="Photo of Marieke smiling in an off-shoulder blue striped top on a sunny terrace"></div>
    </figure>
    <figure class="polaroid polaroid--together">
      <div class="photo" role="img" aria-label="Selfie of Marieke and Dorian together, her in a red scarf"></div>
    </figure>

    <section class="letter">
      <p>Once in your lifetime you meet someone who changes everything. She is going to do her thing with or without you. That's why she is a queen. But... we are just better together. That's why I want you to love me, stay with me and marry me. Would you?</p>
      <p>Marieke,</p>
      <p>Wil je met me trouwen?</p>
      <p>-xxx-</p>
      <p>Dorian</p>
    </section>
  </main>
</body>
</html>
```